Seeking a new modern and sophisticated business card design!

We are looking for a modern, sophisticated business card design. We are open to single sided and double sided designs.

We would like to include our slogan which is "Think Excellence."

Business

```html
<!DOCTYPE html>
<html lang="en">
<head>
<meta charset="utf-8">
<title>The Velora Group Inc — Business Card</title>
<link rel="stylesheet" href="https://fonts.googleapis.com/css2?family=Open+Sans:wght@400;600&display=swap">
<style>
  :root {
    --lime: #78fc00;
    --lime-text: #7ee83a;
    --slate: #434d55;
    --paper: #fbfbfb;
    --paper-shade: #f0f0f0;
    --mark-faint: #dcdddd;
  }
  * { margin: 0; padding: 0; box-sizing: border-box; }
  html, body { width: 972px; height: 1200px; overflow: hidden; background: var(--paper); }
  body { font-family: "Open Sans", Arial, sans-serif; color: var(--slate); }

  .canvas { position: relative; width: 972px; height: 1200px; }

  .card-side {
    position: absolute; left: 0; width: 972px;
    background: linear-gradient(180deg, var(--paper) 0%, var(--paper-shade) 35%, var(--paper) 60%, var(--paper-shade) 100%);
    overflow: hidden;
  }
  .card-front { top: 0; height: 540px; }
  .card-back { top: 608px; height: 540px; }

  .band { position: absolute; left: 0; width: 972px; background: var(--lime); }
  .band-middle { top: 540px; height: 55px; }
  .band-bottom { top: 1148px; height: 52px; }

  /* Front: brand lockup */
  .brand-dot {
    position: absolute; left: 139px; top: 165px;
    width: 240px; height: 240px; border-radius: 50%;
    background: var(--lime);
  }
  .brand-name {
    position: absolute; left: 402px; top: 168px;
    font-weight: 600; font-size: 64px; line-height: 76px;
    color: var(--slate); letter-spacing: 1px; text-transform: uppercase;
  }

  /* Back: faint brand circle */
  .back-dot {
    position: absolute; left: 518px; top: 127px;
    width: 414px; height: 414px; border-radius: 50%;
    background: var(--mark-faint); opacity: 0.75;
  }

  .person { position: absolute; left: 53px; top: 62px; }
  .person-name { font-size: 50px; line-height: 60px; font-weight: 400; color: var(--slate); letter-spacing: -0.5px; }
  .person-role { font-size: 41px; line-height: 54px; font-weight: 400; color: var(--lime-text); letter-spacing: -0.5px; }

  .contact { position: absolute; left: 53px; top: 346px; list-style: none; }
  .contact li { font-size: 41px; line-height: 55px; letter-spacing: -0.5px; white-space: nowrap; }
  .contact-label { color: var(--lime-text); }
  .contact-value { color: var(--slate); }
</style>
</head>
<body>
<main class="canvas">
  <section class="card-side card-front">
    <span class="brand-dot" aria-hidden="true"></span>
    <h1 class="brand-name">The Velora<br>Group Inc</h1>
  </section>

  <div class="band band-middle"></div>

  <section class="card-side card-back">
    <span class="back-dot" aria-hidden="true"></span>
    <div class="person">
      <p class="person-name">Jane Doe</p>
      <p class="person-role">JOB DESCRIPTION</p>
    </div>
    <ul class="contact">
      <li><span class="contact-label">TEL:</span> <span class="contact-value">123.456.7890</span></li>
      <li><span class="contact-label">EMAIL:</span> <span class="contact-value">jane@veloragroup.com</span></li>
      <li><span class="contact-label">WEB:</span> <span class="contact-value">www.veloragroup.com</span></li>
    </ul>
  </section>

  <div class="band band-bottom"></div>
</main>
</body>
</html>
```